My dynamic new collection of short plays needs an eye catching web-based ad!

I am buying ad space on a theater magazine's website with these specs for a new book. The ad will run for a few months. I have the book cover - which will be the main image, but need the ad designed with quotes and the publisher's logo. Here are the specs:
230 pixels wide x 250 pixels high
72 dpi

Target Market(s)

Theater artists and theater educators

Industry/Entity Type

Theater / Education

Font styles to use
Sans Serif
Other font styles liked:
• Please use fonts that match the book cover. I'm including an ad that is currently on the website where I will be advertising. It is not the size that I'm going for, but it contains the elements that I want. I'm also including an image of the logo of the publisher, and I have other versions of this logo (other formats / larger size) that I can deliver if needed.

Requirements
Must have
• Simple compelling image with a quote from the book and a link to the publisher website. A compelling quote (or two) from the book jacket. The name and logo of the publisher.
Nice to have
• Some eye catching color to compliment the beautiful cover design
Should not have
• Too much busy-ness in the image or the presentation.

```html
<!DOCTYPE html>
<html lang="en">
<head>
<meta charset="utf-8">
<title>A Few Small Scenes to Mend the World — Marcus Dale</title>
<link rel="stylesheet" href="https://fonts.googleapis.com/css2?family=Archivo+Black&family=Cinzel:wght@500;700&family=Libre+Baskerville:wght@400;700&family=Raleway:wght@500;800&display=swap">
<style>
  :root {
    --backdrop: #e3e7e2;
    --ink: #2a2a2a;
    --band-dark: #2b2b2b;
    --crimson: #9b1b22;
    --deep-red: #6e1a1f;
    --body: #3a3a3a;
    --rule: #2a2a2a;
    --cover-deep: #12318c;
    --cover-mid: #2058c9;
    --cover-light: #48b6e8;
    --cover-type: #1d3f9e;
    --white: #ffffff;
  }
  * { margin: 0; padding: 0; box-sizing: border-box; }
  html, body { width: 1200px; height: 1200px; overflow: hidden; background: var(--backdrop); }
  .ad {
    position: absolute; left: 147px; top: 108px; width: 906px; height: 984px;
    background: linear-gradient(180deg, #fafafa 0%, #efefef 70%, #f4f4f4 100%);
    box-shadow: 0 2px 10px rgba(0,0,0,0.12);
  }
  .author-possessive {
    position: absolute; left: 56px; top: 46px; white-space: nowrap;
    font-family: "Cinzel", serif; font-weight: 700; font-size: 41px; line-height: 50px; letter-spacing: 1.5px;
    color: var(--crimson);
  }
  .headline { font-weight: normal; }
  .title-line {
    position: absolute; left: 0; font-family: "Raleway", sans-serif; font-weight: 800;
    font-size: 52px; line-height: 54px; letter-spacing: 0.5px; padding-left: 56px; white-space: nowrap;
  }
  .title-line.few { top: 118px; color: var(--ink); }
  .title-line.scenes { top: 174px; height: 49px; line-height: 50px; width: 448px; background: var(--band-dark); color: var(--white); }
  .title-line.mend { top: 228px; color: var(--crimson); }
  .title-line.world { top: 283px; height: 48px; line-height: 49px; width: 404px; background: var(--crimson); color: var(--white); }

  .book-cover {
    position: absolute; left: 51px; top: 372px; width: 398px; height: 560px;
    background: radial-gradient(circle at 55% 55%, var(--cover-light) 0%, var(--cover-mid) 45%, var(--cover-deep) 100%);
    box-shadow: 0 14px 18px -10px rgba(0,0,0,0.45);
    border-radius: 2px;
  }
  .cover-line {
    position: absolute; background: var(--white); color: var(--cover-type); white-space: nowrap;
    font-family: "Archivo Black", sans-serif; font-size: 23px; line-height: 26px; letter-spacing: 1.5px; padding: 0 6px;
  }
  .cover-line.a-few { left: 54px; top: 53px; font-size: 21px; letter-spacing: 1px; }
  .cover-line.small-scenes { left: 35px; top: 83px; }
  .cover-line.to { left: 224px; top: 113px; font-size: 21px; letter-spacing: 1px; }
  .cover-line.mend-world { left: 24px; top: 143px; }
  .cover-author {
    position: absolute; left: 0; right: 0; top: 600px; text-align: center;
  }
  .book-cover .cover-author {
    top: auto; bottom: 22px;
    font-family: "Archivo Black", sans-serif; font-size: 32px; letter-spacing: 2.5px; color: var(--white);
  }

  .availability {
    position: absolute; left: 448px; width: 458px; top: 50px; text-align: center;
    font-family: "Libre Baskerville", serif; font-weight: 700; font-size: 17px; color: var(--ink);
  }
  .publisher-dot {
    position: absolute; left: 595px; top: 108px; width: 190px; height: 190px; border-radius: 50%; background: var(--band-dark);
  }
  .publisher-name {
    position: absolute; left: 448px; width: 458px; top: 353px; text-align: center;
    font-family: "Libre Baskerville", serif; font-weight: 400; font-size: 20px; line-height: 32px; letter-spacing: 3px;
    color: var(--ink); text-transform: uppercase;
  }

  .endorsement { position: absolute; left: 516px; width: 324px; }
  .endorsement.first { top: 467px; }
  .endorsement.second { top: 724px; }
  .endorser-name { font-family: "Cinzel", serif; font-weight: 500; font-size: 20px; line-height: 24px; color: var(--ink); letter-spacing: 1px; }
  .endorser-name b { color: var(--deep-red); font-weight: 700; }
  .endorser-role { font-family: "Libre Baskerville", serif; font-weight: 700; font-size: 14px; line-height: 18px; color: var(--ink); }
  .endorsement.second .endorser-name, .endorsement.second .endorser-role { text-align: right; }
  .endorsement-rule { height: 2px; margin-top: 5px; background: linear-gradient(90deg, var(--rule) 0%, var(--rule) 55%, var(--crimson) 100%); }
  .quote-mark { display: block; width: 22px; height: 18px; }
  .quote-mark.open { margin-top: 21px; }
  .quote-mark.close { margin: -4px 0 0 auto; }
  .quote-text {
    margin-top: 6px; padding-right: 6px;
    font-family: "Raleway", sans-serif; font-weight: 500; font-size: 17px; line-height: 21.8px; color: var(--body);
  }
</style>
</head>
<body>
<main class="ad">
  <p class="author-possessive">MARCUS DALE’S</p>
  <h1 class="headline">
    <span class="title-line few">A FEW</span>
    <span class="title-line scenes">SMALL SCENES</span>
    <span class="title-line mend">TO MEND</span>
    <span class="title-line world">THE WORLD</span>
  </h1>

  <div class="book-cover" role="img" aria-label="Book cover: colourful geometric portrait of the author against a deep blue sky with a glowing arc">
    <span class="cover-line a-few">a few</span>
    <span class="cover-line small-scenes">SMALL SCENES</span>
    <span class="cover-line to">to</span>
    <span class="cover-line mend-world">MEND THE WORLD</span>
    <div class="cover-author">MARCUS DALE</div>
  </div>

  <p class="availability">Available now from</p>
  <div class="publisher-dot"></div>
  <p class="publisher-name">Quiet Lantern<br>Press</p>

  <section class="endorsement first">
    <p class="endorser-name"><b>WARREN</b> T. HALE</p>
    <p class="endorser-role">Theater Maker /Facilitator /Collaborator</p>
    <div class="endorsement-rule"></div>
    <svg class="quote-mark open" viewBox="0 0 26 20" aria-hidden="true"><path fill="#9b1b22" d="M2 20V12Q2 3 11 0l1 3Q7 5 7 10h5v10zM16 20V12q0-9 9-12l1 3q-5 2-5 7h5v10z"/></svg>
    <p class="quote-text">Marcus Dale’s writing has an underlying, yet profound sadness to it. It is powerful in his work and keys into the inherit loneliness that all human beings experience at one time or another.</p>
    <svg class="quote-mark close" viewBox="0 0 26 20" aria-hidden="true"><path fill="#9b1b22" d="M24 0v8q0 9-9 12l-1-3q5-2 5-7h-5V0zM10 0v8q0 9-9 12L0 17q5-2 5-7H0V0z"/></svg>
  </section>

  <section class="endorsement second">
    <p class="endorser-name"><b>DORIAN</b> PRICE</p>
    <p class="endorser-role">Actor and Stage Director</p>
    <div class="endorsement-rule"></div>
    <svg class="quote-mark open" viewBox="0 0 26 20" aria-hidden="true"><path fill="#9b1b22" d="M2 20V12Q2 3 11 0l1 3Q7 5 7 10h5v10zM16 20V12q0-9 9-12l1 3q-5 2-5 7h5v10z"/></svg>
    <p class="quote-text">Marcus provokes us to look more carefully at systems of race and power and our participation in them in ways that linger long after the blackout.</p>
    <svg class="quote-mark close" viewBox="0 0 26 20" aria-hidden="true"><path fill="#9b1b22" d="M24 0v8q0 9-9 12l-1-3q5-2 5-7h-5V0zM10 0v8q0 9-9 12L0 17q5-2 5-7H0V0z"/></svg>
  </section>
</main>
</body>
</html>
```